Now Leasing Banner

Looking for a banner that says the following information approx 4' x 30'

Now Leasing Maplewood Terrace 925-318-6054

Target Market(s)

Drive by traffic

Industry/Entity Type

Residential property management

Requirements
Must have
• Clear and readable from a distance

```html
<!DOCTYPE html>
<html lang="en">
<head>
<meta charset="utf-8">
<title>Now Leasing Banner – Maplewood Terrace</title>
<link rel="stylesheet" href="https://fonts.googleapis.com/css2?family=Anton&family=Oswald:wght@500;600&display=swap">
<style>
  :root {
    --page-bg: #ffffff;
    --brand-red: #a30803;
    --panel-light: #f2f3f3;
    --panel-light-edge: #e4e7e8;
    --panel-border: #b9bcbe;
    --ink-shadow: #141010;
    --text-light: #ffffff;
    --drop-shadow: rgba(0, 0, 0, 0.45);
  }
  * { margin: 0; padding: 0; box-sizing: border-box; }
  html, body {
    width: 1200px;
    height: 323px;
    overflow: hidden;
    background: var(--page-bg);
  }
  .canvas {
    position: relative;
    width: 1200px;
    height: 323px;
  }
  .banner {
    position: absolute;
    left: 76px;
    top: 81px;
    width: 1022px;
    height: 137px;
    display: flex;
    box-shadow: 8px 8px 8px var(--drop-shadow);
  }
  .banner__headline {
    width: 482px;
    height: 100%;
    background: var(--brand-red);
    color: var(--text-light);
    display: flex;
    flex-direction: column;
    align-items: center;
    justify-content: center;
    font-family: "Oswald", "Arial Narrow", sans-serif;
  }
  .banner__title {
    font-weight: 600;
    font-size: 56px;
    line-height: 1;
    letter-spacing: 6px;
    margin-right: -6px;
    margin-top: -6px;
  }
  .banner__property {
    font-weight: 500;
    font-size: 40px;
    line-height: 1;
    margin-top: 6px;
  }
  .banner__contact {
    flex: 1;
    height: 100%;
    border: 1px solid var(--panel-border);
    border-left: none;
    background: radial-gradient(ellipse at 40% 40%, var(--panel-light) 0%, var(--panel-light-edge) 100%);
    display: flex;
    align-items: center;
    justify-content: center;
  }
  .banner__phone {
    display: block;
    width: 500px;
    height: 110px;
  }
  .banner__phone-text {
    font-family: "Anton", "Impact", sans-serif;
    font-size: 102px;
  }
  .banner__phone-shadow { fill: var(--ink-shadow); }
  .banner__phone-face { fill: var(--brand-red); }
</style>
</head>
<body>
  <main class="canvas">
    <section class="banner">
      <div class="banner__headline">
        <h1 class="banner__title">NOW LEASING</h1>
        <p class="banner__property">Maplewood Terrace</p>
      </div>
      <div class="banner__contact">
        <svg class="banner__phone" viewBox="0 0 500 110" aria-label="925-318-6054">
          <text class="banner__phone-text banner__phone-shadow" x="14" y="102" textLength="480" lengthAdjust="spacingAndGlyphs">925-318-6054</text>
          <text class="banner__phone-text banner__phone-face" x="10" y="98" textLength="480" lengthAdjust="spacingAndGlyphs">925-318-6054</text>
        </svg>
      </div>
    </section>
  </main>
</body>
</html>
```